IT Management and Consulting company wants a design

The website should transfer an innovative, forward-oriented, optimistic, and serious image to my customer. Because we work in an agile, the design should transfer this approach.

The new color should make a serious, but not boring, impression for the business visitors of top-level companies.

The main focus topics are:
* IT strategy consulting
* Digital transformation
* IT quality management

The website should be in the English language.

The website should be created for WordPress. The existing website is http://www.t-vork.com (no WordPress) is provided by servalpin.de. A WordPress sandbox system exists.

Target Market(s)

Purchasing departments, IT decision makers from companies, project recruiting companies

Industry/Entity Type

IT-Provider, Telecommunication, Automotive

Coding

Coded - Design and coding required

Number of Pages Required

4 page

Font styles to use
Serif
Sans Serif

Requirements
Must have
• Long-pager scrolling, a detail page for each portfolio topics, contact page, page about the company
Nice to have
• Parallax animation less is more, maybe a nice Hero Video Header, interessting 3D graph, Isometric graphs will bi nice, more clean than overloaded,
Should not have
• personal recruting page like in www.t-vork.com

```html
<!DOCTYPE html>
<html lang="en">
<head>
<meta charset="utf-8">
<title>Halden Consulting</title>
<link href="https://fonts.googleapis.com/css2?family=Figtree:wght@300;400;500;700&display=swap" rel="stylesheet">
<style>
:root{
  --navy-deep:#020f24;
  --navy-footer:#020f26;
  --bar-bottom:#0b0710;
  --blue:#0a56b8;
  --blue-text:#1160c4;
  --white:#ffffff;
  --ink:#2b2b33;
  --hero-a:#03122e;
  --hero-b:#0a3b86;
  --hero-c:#1aa4d6;
}
*{margin:0;padding:0;box-sizing:border-box}
html,body{width:678px;height:1200px;overflow:hidden;background:var(--white)}
body{position:relative;font-family:"Figtree",Arial,sans-serif;color:var(--ink)}
.abs{position:absolute}

/* hero */
.hero{left:0;top:0;width:678px;height:328px;
  background:radial-gradient(circle at 50% 48%, var(--hero-a) 0 14%, var(--hero-b) 30%, #06204f 48%, var(--hero-c) 62%, #072a66 72%, #020d26 100%)}
.logo{color:var(--white);font-weight:400;line-height:1}
.logo .name{display:block;font-size:15px;letter-spacing:1px}
.logo .sub{display:block;font-size:5px;letter-spacing:2px;margin-top:2px}
.nav a{position:absolute;top:22px;font-size:5.4px;color:var(--white);text-decoration:none;letter-spacing:.2px}
.nav .active::after{content:"";position:absolute;left:0;right:0;top:8px;height:.8px;background:var(--hero-c)}
.hero-title{left:0;width:678px;top:133px;text-align:center;color:var(--white);font-weight:700;font-size:17px;line-height:33px}
.btn{position:absolute;background:var(--blue);color:var(--white);display:flex;align-items:center;justify-content:center;border-radius:1.5px}
.hero .btn{left:302px;top:216px;width:72px;height:17px;font-size:5.6px}

/* intro */
.section-heading{color:var(--blue-text);font-weight:300;font-size:13.4px;line-height:15.6px}
.copy{font-size:6.6px;line-height:9.2px;color:var(--ink);width:215px}

/* topics band */
.topics{left:0;top:454px;width:678px;height:156px;background:var(--navy-deep);border-bottom:.6px solid #6d7e98}
.topics .btn{top:73px;height:17px;font-size:8.4px;font-weight:300}

/* photo band */
.who{left:0;top:611px;width:678px;height:162px;
  background:linear-gradient(180deg,#071843 0%,#0c3b95 45%,#081f55 100%)}
.who-title{left:0;width:678px;top:74px;text-align:center;color:var(--white);font-weight:700;font-size:13.4px;letter-spacing:5.5px}

/* footer */
.footer{left:0;top:1006px;width:678px;height:177px;background:var(--navy-footer);color:var(--white)}
.footer h3{position:absolute;font-weight:400;font-size:8.6px;letter-spacing:.2px}
.footer .item{position:absolute;font-size:5.6px;line-height:7px;white-space:nowrap}
.footer svg{position:absolute}
.field{position:absolute;left:470px;width:116px;background:var(--white);border-radius:1.5px;font-size:4.6px;color:#777;padding:3px 3px}
.send{position:absolute;left:470px;top:141px;width:115px;height:15px;border:.7px solid var(--white);border-radius:1.5px;font-size:5.6px;display:flex;align-items:center;justify-content:center}
.bottom-bar{left:0;top:1183px;width:678px;height:17px;background:var(--bar-bottom)}
</style>
</head>
<body>

<header class="abs hero" role="img" aria-label="Glowing blue digital tunnel of light streaks">
  <div class="abs logo" style="left:153px;top:16px"><span class="name">HALDEN</span><span class="sub">CONSULTING</span></div>
  <nav class="nav">
    <a class="active" style="left:293px">HOME</a>
    <a style="left:333px">COMPANIES</a>
    <a style="left:387px">PORTFOLIO</a>
    <a style="left:441px">SCOUTING</a>
    <a style="left:493px">CONTACT</a>
  </nav>
  <h1 class="abs hero-title">IT SYSTEMS THAT DO<br>WHAT THEY SHOULD</h1>
  <a class="btn">VIEW SERVICES</a>
</header>

<section>
  <h2 class="abs section-heading" style="left:154px;top:366px">DIGITAL<br>TRANSFORMATION</h2>
  <p class="abs copy" style="left:314px;top:368px">With our methodological competence in classic and agile projects, we can support you and help you to shape the transition from the old world of ideas to the new agile mindset. Change projects require competent management.</p>
</section>

<section class="abs topics">
  <a class="btn" style="left:95px;width:72px">IT STRATEGY</a>
  <a class="btn" style="left:270px;width:136px">DIGITAL TRANSFORMATION</a>
  <a class="btn" style="left:511px;width:72px">IT QUALITY</a>
</section>

<section class="abs who" role="img" aria-label="Rows of computer monitors with streams of binary code in blue light">
  <h2 class="abs who-title">WHO WE ARE</h2>
</section>

<section>
  <h2 class="abs section-heading" style="left:154px;top:811px">A PROFESSIONAL<br>METHOD<br>FOR PROJECT<br>SUCCESS</h2>
  <p class="abs copy" style="left:314px;top:813px">Whether IT project management, consulting, commissioning management or system integration: With Halden Consulting you create the best conditions for IT systems that do what they should. In compliance with all time and cost specifications.</p>
  <p class="abs copy" style="left:314px;top:857px;width:205px">Well-known companies from the automotive industry and telecommunications regularly use our know-how in the form of individual management and consulting services.</p>
  <p class="abs copy" style="left:314px;top:901px">Our comprehensive approach combines technical depth with a perspective that always keeps the big picture in mind. For example, the business benefits of your application. In addition to our technical excellence, customers also value our methodical and communicative skills - because behind every IT project there are people who want to be integrated. If more than 25 years of experience is just good enough for you, we look forward to hearing from you!</p>
</section>

<footer class="abs footer">
  <div class="abs logo" style="left:91px;top:35px"><span class="name">HALDEN</span><span class="sub">CONSULTING</span></div>

  <h3 style="left:198px;top:34px">OUR COMPANY</h3>
  <svg style="left:198px;top:62px" width="9" height="9" viewBox="0 0 10 10" fill="none" stroke="#fff" stroke-width=".8"><path d="M1 5 L5 1.5 L9 5 M2.2 4.2 V9 H7.8 V4.2 M4.2 9 V6.5 H5.8 V9"/></svg>
  <span class="item" style="left:212px;top:64px">Halden Consulting</span>
  <svg style="left:198px;top:86px" width="9" height="11" viewBox="0 0 10 12" fill="none" stroke="#fff" stroke-width=".8"><path d="M5 11 C2 7.5 1.5 6 1.5 4.5 A3.5 3.5 0 0 1 8.5 4.5 C8.5 6 8 7.5 5 11 Z"/><circle cx="5" cy="4.5" r="1.3"/><path d="M2.5 11.3 H7.5"/></svg>
  <span class="item" style="left:212px;top:85px">214 Example Street, 14th Floor<br>Sample City, Germany 654321</span>
  <svg style="left:198px;top:110px" width="8" height="8" viewBox="0 0 10 10" fill="none" stroke="#fff" stroke-width=".8"><path d="M2 1 L3.8 1 L4.6 3.2 L3.4 4.2 C4 5.6 4.6 6.2 5.8 6.8 L6.8 5.6 L9 6.4 V8.2 C9 8.7 8.6 9 8 9 C4.5 8.7 1.3 5.5 1 2 C1 1.4 1.4 1 2 1 Z"/></svg>
  <span class="item" style="left:212px;top:111px">(555) 010-2468</span>
  <svg style="left:197px;top:131px" width="11" height="11" viewBox="0 0 12 12" fill="none" stroke="#fff" stroke-width=".8"><circle cx="6" cy="6" r="5.3"/></svg>
  <span class="item" style="left:212px;top:133px">HaldenConsulting</span>

  <h3 style="left:339px;top:34px">QUICK LINKS</h3>
  <svg style="left:340px;top:66px" width="4" height="5" viewBox="0 0 4 5"><path d="M0 0 L3 2.5 L0 5 Z" fill="#fff"/></svg>
  <span class="item" style="left:348px;top:64px">Home</span>
  <svg style="left:340px;top:83px" width="4" height="5" viewBox="0 0 4 5"><path d="M0 0 L3 2.5 L0 5 Z" fill="#fff"/></svg>
  <span class="item" style="left:348px;top:82px">Companies</span>
  <svg style="left:340px;top:99px" width="4" height="5" viewBox="0 0 4 5"><path d="M0 0 L3 2.5 L0 5 Z" fill="#fff"/></svg>
  <span class="item" style="left:348px;top:98px">Portfolio</span>
  <svg style="left:340px;top:116px" width="4" height="5" viewBox="0 0 4 5"><path d="M0 0 L3 2.5 L0 5 Z" fill="#fff"/></svg>
  <span class="item" style="left:348px;top:115px">Scouting</span>

  <h3 style="left:469px;top:34px">CONTACT US</h3>
  <div class="field" style="top:50px;height:13px">Name*</div>
  <div class="field" style="top:66px;height:13px">Email*</div>
  <div class="field" style="top:81px;height:13px">Phone*</div>
  <div class="field" style="top:97px;height:40px">Comments</div>
  <div class="send">SEND MESSAGE</div>
</footer>
<div class="abs bottom-bar"></div>

</body>
</html>
```